PowerPoint design of key models

We recently had a new PPT template created which we are very happy with. Now we want to have some of our key models on various pages in PPT to be reformatted and redesigned to match the other graphics of the new PT template. Can you please redesign the models and graphics so they have the same look and feel as the new template. I have included both files for you to work with. Thank you.

```html
<!DOCTYPE html>
<html lang="en">
<head>
<meta charset="utf-8">
<title>Key Models</title>
<link href="https://fonts.googleapis.com/css2?family=Montserrat:wght@400;500;600&display=swap" rel="stylesheet">
<style>
:root{
  --page:#ebebeb;
  --card:#ffffff;
  --ink:#1a1a1a;
  --muted:#3a3a3a;
  --grey:#c2c2c2;
  --lilac:#b29fca;
  --sage:#b6d7a1;
  --green:#3daf4a;
  --blue:#0b6fc3;
  --sky:#4eaae6;
  --amber:#ecb845;
  --indigo:#3b2d7f;
  --icon-bg:#f2f2f2;
  --icon-tone:#dcdcdc;
}
*{margin:0;padding:0;box-sizing:border-box}
html,body{width:1200px;height:738px;overflow:hidden;background:var(--page)}
body{font-family:"Montserrat",sans-serif;color:var(--ink);position:relative}
.card{position:absolute;background:var(--card)}
.shapes{position:absolute;left:0;top:0;width:1200px;height:738px}
.t{position:absolute;white-space:nowrap;line-height:1}
.pill{position:absolute;left:50px;width:127px;height:45px;border-radius:23px;color:#fff;font-size:15.5px;display:flex;align-items:center;justify-content:center;letter-spacing:.2px}
.pill.detection{background:var(--grey)}
.pill.connection{background:var(--lilac)}
.pill.alignment{background:var(--sage)}
.pill.collaboration{background:var(--green)}
.pill.authenticity{background:var(--blue)}
.cue{left:260px;font-size:9.4px;color:var(--ink)}
.focus-label{font-size:21.5px;transform:translateX(-50%);letter-spacing:.6px}
.fab-title{font-size:18px;transform:translateX(-50%)}
.fab-desc{font-size:6.8px;color:var(--muted);text-align:center;transform:translateX(-50%);line-height:1.45;white-space:normal}
.tool-label{font-size:11.5px;font-weight:600;text-align:center;transform:translateX(-50%);line-height:1.1}
.page-no{right:26px;top:709px;font-size:11.5px;font-weight:500}
</style>
</head>
<body>
<div class="card" style="left:22px;top:20px;width:569px;height:319px"></div>
<div class="card" style="left:611px;top:20px;width:569px;height:319px"></div>
<div class="card" style="left:19px;top:374px;width:568px;height:320px"></div>
<div class="card" style="left:607px;top:375px;width:569px;height:320px"></div>

<svg class="shapes" viewBox="0 0 1200 738">
  <defs>
    <linearGradient id="task-ring" x1="0" y1="0" x2="0" y2="1"><stop offset="0" stop-color="#e6e6e6"/><stop offset="1" stop-color="#0b6fc3"/></linearGradient>
    <linearGradient id="team-ring" x1="0" y1="0" x2="0" y2="1"><stop offset="0" stop-color="#b9a9d2"/><stop offset="1" stop-color="#5a12b0"/></linearGradient>
    <linearGradient id="ind-ring" x1="0" y1="0" x2="0" y2="1"><stop offset="0" stop-color="#d2f7d6"/><stop offset="1" stop-color="#3daf4a"/></linearGradient>
  </defs>

  <!-- approach connectors -->
  <g fill="none" stroke-width="0.8" stroke-dasharray="2.5 2">
    <g stroke="var(--grey)"><path d="M177 66H226L246 57M226 66L246 75"/></g>
    <g stroke="var(--lilac)"><path d="M177 121H226L246 113M226 121L246 130"/></g>
    <g stroke="var(--sage)"><path d="M177 177H226L246 169M226 177L246 186"/></g>
    <g stroke="var(--green)"><path d="M177 233H226L246 225M226 233L246 242"/></g>
    <g stroke="var(--blue)"><path d="M177 289H226L246 281M226 289L246 298"/></g>
  </g>
  <g fill="var(--grey)" opacity=".6"><circle cx="226" cy="66" r="3.5"/><circle cx="246" cy="57" r="3.5"/><circle cx="246" cy="75" r="3.5"/></g>
  <g fill="var(--lilac)"><circle cx="226" cy="121" r="3.5"/><circle cx="246" cy="113" r="3.5"/><circle cx="246" cy="130" r="3.5"/></g>
  <g fill="var(--sage)"><circle cx="226" cy="177" r="3.5"/><circle cx="246" cy="169" r="3.5"/><circle cx="246" cy="186" r="3.5"/></g>
  <g fill="var(--green)"><circle cx="226" cy="233" r="3.5"/><circle cx="246" cy="225" r="3.5"/><circle cx="246" cy="242" r="3.5"/></g>
  <g fill="var(--blue)"><circle cx="226" cy="289" r="3.5"/><circle cx="246" cy="281" r="3.5"/><circle cx="246" cy="298" r="3.5"/></g>

  <!-- focus rings -->
  <g fill="none">
    <circle cx="725" cy="182" r="61" stroke="url(#task-ring)" stroke-width="8"/>
    <path d="M662 135A76 76 0 0 0 662 228" stroke="url(#task-ring)" stroke-width="7"/>
    <circle cx="896" cy="190" r="62" stroke="url(#team-ring)" stroke-width="9"/>
    <path d="M851 130A72 72 0 0 1 941 130" stroke="url(#team-ring)" stroke-width="7"/>
    <circle cx="1065" cy="182" r="61" stroke="url(#ind-ring)" stroke-width="8"/>
    <path d="M1128 135A76 76 0 0 1 1128 228" stroke="url(#ind-ring)" stroke-width="7"/>
  </g>
  <rect x="697" y="154" width="56" height="56" rx="6" fill="var(--icon-tone)" role="img" aria-label="Checklist icon"/>
  <rect x="868" y="162" width="56" height="56" rx="6" fill="var(--icon-tone)" role="img" aria-label="Team and gear icon"/>
  <rect x="1037" y="154" width="56" height="56" rx="6" fill="var(--icon-tone)" role="img" aria-label="Focused individual icon"/>

  <!-- FAB hexagons -->
  <g fill="none" stroke-width="1.5">
    <g stroke="var(--green)"><path d="M54 455L98 428L142 455M54 525L98 552L142 525M98 552V581"/></g>
    <g stroke="var(--amber)"><path d="M195 533L239 506L283 533M195 603L239 630L283 603M239 506V480"/></g>
    <g stroke="var(--sky)"><path d="M327 455L371 428L415 455M327 525L371 552L415 525M371 552V581"/></g>
    <g stroke="var(--indigo)"><path d="M468 533L512 506L556 533M468 603L512 630L556 603M512 506V480"/></g>
  </g>
  <path d="M98 436L146 463V517L98 544L50 517V463Z" fill="var(--green)"/>
  <path d="M239 514L287 541V595L239 622L191 595V541Z" fill="var(--amber)"/>
  <path d="M371 436L419 463V517L371 544L323 517V463Z" fill="var(--sky)"/>
  <path d="M512 514L560 541V595L512 622L464 595V541Z" fill="var(--indigo)"/>
  <g fill="#ffffff" opacity=".25">
    <rect x="72" y="462" width="52" height="52" rx="5" role="img" aria-label="Puzzle pieces icon"/>
    <rect x="213" y="540" width="52" height="52" rx="5" role="img" aria-label="Award and growth arrows icon"/>
    <rect x="345" y="462" width="52" height="52" rx="5" role="img" aria-label="Hand with money and growth icon"/>
    <rect x="486" y="540" width="52" height="52" rx="5" role="img" aria-label="Clipboard and idea icon"/>
  </g>

  <!-- coaching tools -->
  <g fill="none" stroke="var(--icon-tone)" stroke-width="1.5" stroke-dasharray="5 4">
    <path d="M727 508L780 530M864 530L914 505M1002 505L1055 530"/>
  </g>
  <g fill="var(--icon-bg)" stroke="var(--indigo)" stroke-width="10">
    <circle cx="685" cy="481" r="46"/><circle cx="822" cy="553" r="46"/>
    <circle cx="960" cy="481" r="46"/><circle cx="1097" cy="553" r="46"/>
  </g>
  <g fill="var(--icon-tone)">
    <rect x="659" y="455" width="52" height="52" rx="6" role="img" aria-label="Call sequence icon"/>
    <rect x="796" y="527" width="52" height="52" rx="6" role="img" aria-label="Coaching cycle icon"/>
    <rect x="934" y="455" width="52" height="52" rx="6" role="img" aria-label="Recruitment search icon"/>
    <rect x="1071" y="527" width="52" height="52" rx="6" role="img" aria-label="Coaching session icon"/>
  </g>
</svg>

<div class="pill detection" style="top:43px">Detection</div>
<div class="pill connection" style="top:99px">Connection</div>
<div class="pill alignment" style="top:155px">Alignment</div>
<div class="pill collaboration" style="top:211px">Collaboration</div>
<div class="pill authenticity" style="top:267px">Authenticity</div>

<div class="t cue" style="top:53px">Get your radar on to read the climate</div>
<div class="t cue" style="top:68px">What can you observe, hear, sense</div>
<div class="t cue" style="top:109px">Use empathy to build a bridge</div>
<div class="t cue" style="top:124px">Get them talking about themselves</div>
<div class="t cue" style="top:165px">Find what you have in common</div>
<div class="t cue" style="top:180px">Maximise similarities and minimise</div>
<div class="t cue" style="top:221px">Create a shared experience - get them involved early</div>
<div class="t cue" style="top:236px">Work on an activity together – probing, solving, options, inspecting</div>
<div class="t cue" style="top:277px">Be genuine and keep it real</div>
<div class="t cue" style="top:292px">Don’t overdo your energy or confidence – be your best you!</div>

<div class="t focus-label" style="left:725px;top:268px">TASK</div>
<div class="t focus-label" style="left:896px;top:268px">TEAM</div>
<div class="t focus-label" style="left:1065px;top:268px">INDIVIDUAL</div>

<div class="t fab-title" style="left:98px;top:587px">Feature</div>
<div class="t fab-desc" style="left:97px;top:614px;width:140px">What it is or has in the product/service itself - An indisputable characteristic or attribute</div>
<div class="t fab-title" style="left:239px;top:415px">Advantage</div>
<div class="t fab-desc" style="left:238px;top:443px;width:120px">How the feature works<br>- what it does, or doesn’t do</div>
<div class="t fab-title" style="left:371px;top:587px">Benefit</div>
<div class="t fab-desc" style="left:370px;top:614px;width:140px">Why they should buy it<br>- The end result or outcome for people or businesses</div>
<div class="t fab-title" style="left:512px;top:415px">Proof</div>
<div class="t fab-desc" style="left:511px;top:443px;width:130px">The evidence to support the claim</div>

<div class="t tool-label" style="left:685px;top:550px">PRES Call Sequence</div>
<div class="t tool-label" style="left:822px;top:622px">10 Step Coaching<br>Process</div>
<div class="t tool-label" style="left:960px;top:550px">RECRUIT<br>BD Process</div>
<div class="t tool-label" style="left:1097px;top:622px">Coaching<br>Action Tool</div>

<div class="t page-no">C 25</div>
</body>
</html>
```